stonewick For High end Builder/developer construction

We will be a residential building company focused on a meticulous approach to high end quality builds with a design collaborative approach with all our clients to push the boundaries on new forms, products and bespoke architectural designs.

We want to be known to thrives upon collaboration with architects, designers and our clients to help them transform big ideas into inspiring spaces. We run every part of the building process, from planning through to construction and completion, is detail-focused and seamlessly managed.

Target Market(s)

High end

Font styles to use
Other font styles liked:
• Gotham Light

Colors

Designer to choose only greyscale colors for use in the design.

Requirements
Must have
• Bold headed incorporating sharp features for the logo to standout in mostly black to ensure the logo pops

```html
<!DOCTYPE html>
<html lang="en">
<head>
<meta charset="utf-8">
<title>Stonewick Letterhead</title>
<link href="https://fonts.googleapis.com/css2?family=Encode+Sans+Condensed:wght@300&family=Montserrat:wght@400;500&display=swap" rel="stylesheet">
<style>
  :root {
    --ink: #0e0e10;
    --accent: #a6a6a6;
    --accent-soft: #e6e6e6;
    --paper: #ffffff;
    --backdrop: #d6d6d6;
    --body-text: #555555;
    --header-text: #ffffff;
  }
  * { margin: 0; padding: 0; box-sizing: border-box; }
  html, body {
    width: 1056px; height: 1200px; overflow: hidden;
    background: var(--backdrop);
  }
  .letterhead {
    position: absolute; left: 103px; top: 0;
    width: 849px; height: 1200px;
    background: var(--paper);
  }
  .masthead {
    position: absolute; left: 0; top: 0;
    width: 100%; height: 192px;
    background: var(--ink);
  }
  .brand {
    position: absolute; left: 82px; top: 62px;
    display: flex; align-items: center; gap: 12px;
  }
  .brand-square { width: 26px; height: 26px; background: var(--accent); }
  .brand-name {
    font-family: 'Montserrat', sans-serif; font-weight: 500;
    font-size: 22px; letter-spacing: 5px; text-transform: uppercase;
    color: var(--header-text);
  }
  .contact {
    position: absolute; left: 588px; top: 52px;
    font-family: 'Montserrat', sans-serif; font-weight: 400;
    font-size: 14px; color: var(--header-text); line-height: 19px;
  }
  .contact-address { margin-bottom: 9px; }
  .contact-line { display: flex; align-items: center; gap: 14px; height: 21px; }
  .contact-line svg { width: 16px; height: 16px; flex: none; }
  .letter {
    position: absolute; left: 82px; top: 398px; width: 689px;
    font-family: 'Encode Sans Condensed', sans-serif; font-weight: 300;
    font-size: 19px; line-height: 29.5px; color: var(--body-text);
  }
  .letter p { text-align: justify; margin-bottom: 29px; }
  .letter .salutation { margin-bottom: 26px; }
  .closing {
    position: absolute; left: 82px; top: 988px;
    font-family: 'Encode Sans Condensed', sans-serif; font-weight: 300;
    font-size: 19px; color: var(--body-text);
  }
  .signature {
    position: absolute; left: 80px; top: 1024px;
    width: 68px; height: 44px;
    background: linear-gradient(135deg, var(--accent-soft), #f6f6f6);
  }
  .footer-band { position: absolute; left: 0; bottom: 0; width: 849px; height: 21px; }
</style>
</head>
<body>
  <div class="letterhead">
    <header class="masthead">
      <div class="brand">
        <span class="brand-square"></span>
        <span class="brand-name">Stonewick</span>
      </div>
      <div class="contact">
        <div class="contact-address">48 Harrow Lane, Suite 210<br>Kingsbridge, NY 10463</div>
        <div class="contact-line">
          <svg viewBox="0 0 16 16" aria-hidden="true"><path d="M4 2 L6 5 L5 6.5 Q6.5 9.5 9.5 11 L11 10 L14 12 L12.5 14 Q5 13 2 3.5 Z" fill="none" stroke="var(--accent)" stroke-width="1.5" stroke-linejoin="round"/><path d="M9.5 2.5 Q13 3 13.5 6.5" fill="none" stroke="var(--accent)" stroke-width="1.3"/></svg>
          <span>(555) 204-3180</span>
        </div>
        <div class="contact-line">
          <svg viewBox="0 0 16 16" aria-hidden="true"><rect x="1" y="3" width="14" height="10" fill="var(--accent)"/><path d="M1 3 L8 9 L15 3" fill="none" stroke="var(--ink)" stroke-width="1.2"/></svg>
          <span>hello@stonewick.co</span>
        </div>
        <div class="contact-line">
          <svg viewBox="0 0 16 16" aria-hidden="true"><circle cx="8" cy="8" r="6.5" fill="none" stroke="var(--accent)" stroke-width="1.2"/><ellipse cx="8" cy="8" rx="3" ry="6.5" fill="none" stroke="var(--accent)" stroke-width="1"/><path d="M1.5 8 H14.5 M2.5 5 H13.5 M2.5 11 H13.5" stroke="var(--accent)" stroke-width="1"/></svg>
          <span>www.stonewick.co</span>
        </div>
      </div>
    </header>

    <main class="letter">
      <p class="salutation">Dear Sir/Mam,</p>
      <p>Contrary to popular belief, Lorem Ipsum is not simply random text. It has roots in a piece of classical Latin literature from 45 BC, making it over 2000 years old. Daniel Hartwell, a Latin professor at Ashford Hill College in Virginia, looked up one of the more obscure Latin words, consectetur.</p>
      <p>Lorem Ipsum comes from sections 1.10.32 and 1.10.33 of "de Finibus Bonorum et Malorum" (The Extremes of Good and Evil) by Aurelius Venn, written in 45 BC. This book is a treatise on the theory of ethics, very popular during the Renaissance. The first line of Lorem Ipsum.</p>
      <p>The standard chunk of Lorem Ipsum used since the 1500s is reproduced below for those interested. Sections 1.10.32 and 1.10.33 from "de Finibus Bonorum et Malorum" by Aurelius Venn are also reproduced in their exact original.</p>
      <p>The standard chunk of Lorem Ipsum used since the 1500s is reproduced below for those interested.</p>
    </main>

    <div class="closing">Best Regards</div>
    <div class="signature" role="img" aria-label="Handwritten signature of the sender"></div>

    <svg class="footer-band" viewBox="0 0 849 21" aria-hidden="true">
      <polygon points="0,0 612,0 592,21 0,21" fill="var(--ink)"/>
      <polygon points="627,0 849,0 849,21 607,21" fill="var(--accent)"/>
    </svg>
  </div>
</body>
</html>
```